Driftwood Bay Private Yacht Charter "Rack Flyer"

This will be a 4" x 9" Rack flyer that is 4 colors and two sided. This is a Private Yacht charter company that is based in St Thomas, U.S. Virgin Islands. Our main product that I would like to promote on one entire side of the flyer is our Private Luxury Full Day "Gilded Galley". our charter company is unique in the fact we offer customizable itineraries and we offer unique activities that keep the family and groups engaged in fun for the entire day. We would like something with our colors.

Target Market(s)

We are trying to reach an upscale clients that are looking for a Luxury Day Charter experience. these people will be most likely staying in Private Villas or staying at the Halloway Crest or PK Bellmont.

Requirements
Must have
• Contact Information:
Ph: (340) 555-0187
email: Info@driftwoodbayvoyages.example
www.driftwoodbayvoyages.example
One side should Promote our Gilded Galley (Gilded Galley is a trademarked name).
All Guests will receive "Harbor Fizz"
> Up to 12 guests
> Full Brunch Spread to include, Assorted fruit tower, Artesian Waffle Board, Frittata's, Loaded Avocado Toast or an All American Breakfast.
> Specialty Cocktails with Bottle Service options available
List all of our Unique activities to include:
Snorkeling
Underwater WaveGlider
Cliff Diving
Paddleboarding
Towable Activities
TEXT TO BE WRITTEN:
Experience yacht charter service at its Finest!
Sail away with us on a Luxury Charter experience complete with a full brunch spread. During our sail we will take you to the hottest destination spots in the Caribbean surrounding St Thomas and St John. Warm, fresh baked afternoon cookies will be served on the way back from our days journeys. Unlimited water, sodas, beer and rum punch will be provided for the entire group to enjoy throughout the day.
_________________

On side two of the brochure you can refer to the downloaded text. We do not want pricing listed on the flyer

```html
<!DOCTYPE html>
<html lang="en">
<head>
<meta charset="utf-8">
<title>Driftwood Bay Rack Flyer</title>
<link rel="stylesheet" href="https://fonts.googleapis.com/css2?family=Oswald:wght@500&family=Source+Sans+3:wght@400;600&family=Cormorant+Garamond:wght@500&display=swap">
<style>
:root{
  --page:#eceef1;
  --navy:#1d3f8f;
  --blue:#2258b8;
  --blue-light:#3a7bd0;
  --red:#e0242c;
  --white:#ffffff;
  --ink:#1f2f6a;
  --grey:#c9ccd3;
  --sans:"Source Sans 3",sans-serif;
  --cond:"Oswald",sans-serif;
  --serif:"Cormorant Garamond",serif;
}
*{box-sizing:border-box;margin:0;padding:0}
html,body{width:1200px;height:1064px;overflow:hidden;background:var(--page)}
.canvas{position:relative;width:1200px;height:1064px}
.flyer{position:absolute;top:82px;width:400px;height:900px;overflow:hidden;
  background:linear-gradient(180deg,var(--blue-light) 0%,var(--blue) 45%,var(--navy) 100%);
  box-shadow:0 6px 18px rgba(0,0,0,.25);font-family:var(--sans);color:var(--white)}
.flyer--front{left:170px}
.flyer--back{left:630px}
.photo{position:absolute;left:0;top:0;width:400px}
.photo--family{height:360px;background:linear-gradient(160deg,#9fc4dc 0%,#d9c9b4 40%,#5f87a8 100%)}
.photo--aerial{height:260px;background:linear-gradient(200deg,#e3c79a 0%,#4ec2c9 35%,#1a8fa8 70%,#0d6e8a 100%)}
.wave{position:absolute;left:0;width:400px}
.polaroid{position:absolute;background:var(--white);padding:8px 8px 22px;box-shadow:2px 4px 10px rgba(0,0,0,.35)}
.polaroid .shot{width:100%;height:100%}
.polaroid .pin{position:absolute;top:-5px;width:10px;height:10px;border-radius:50%;background:var(--red)}
.brand{position:absolute;display:flex;align-items:center;gap:8px;white-space:nowrap}
.brand-name{font-family:var(--sans);font-weight:600;font-size:26px;color:var(--white);letter-spacing:.5px}
.brand-dot{width:14px;height:14px;border-radius:50%;background:var(--red);flex:none}
.headline{position:absolute;right:16px;top:442px;text-align:right;font-family:var(--cond);font-weight:500;font-size:31px;line-height:33px;letter-spacing:.2px;white-space:nowrap}
.headline .accent{color:var(--red)}
.tagline{position:absolute;left:0;top:553px;width:400px;text-align:center;font-size:16.5px;padding-bottom:6px;border-bottom:1px solid rgba(255,255,255,.25)}
.intro{position:absolute;left:14px;top:592px;width:370px;font-size:11.4px;line-height:12.4px;text-align:justify}
.lists{position:absolute;left:14px;top:684px;display:flex;gap:18px}
.list h3{font-family:var(--serif);font-weight:500;font-size:15.5px;text-transform:uppercase;display:flex;align-items:center;gap:6px;margin-bottom:4px;white-space:nowrap}
.list h3::before{content:"";width:9px;height:9px;border-radius:50%;background:var(--red)}
.list ul{list-style:none;padding-left:14px}
.list li{font-size:11.5px;line-height:15.4px;position:relative;padding-left:12px;color:#e6ecf8}
.list li::before{content:"";position:absolute;left:0;top:5px;width:5px;height:5px;border-radius:50%;background:var(--red)}
.footer-band{position:absolute;left:0;bottom:0;width:400px;height:80px}
.phone-pill{position:absolute;left:87px;top:819px;width:231px;height:32px;border-radius:16px;background:var(--red);display:flex;align-items:center;justify-content:center;gap:8px;font-size:19px;box-shadow:0 3px 5px rgba(0,0,0,.3)}
.contact{position:absolute;left:0;top:864px;width:400px;text-align:center;font-size:12.5px;color:var(--ink);white-space:nowrap}
.contact .sep{margin:0 4px}
.intro-line{position:absolute;left:20px;top:318px;font-size:15px;line-height:20px}
.services-tab{position:absolute;left:0;top:377px;width:218px;height:36px;background:var(--red);border-radius:0 18px 18px 0;font-family:var(--cond);font-weight:500;font-size:20px;line-height:36px;padding-left:20px;box-shadow:0 3px 5px rgba(0,0,0,.3)}
.service{position:absolute;left:16px;width:366px}
.service h2{font-family:var(--serif);font-weight:500;font-size:18px;text-transform:uppercase;letter-spacing:.2px;margin-bottom:3px;white-space:nowrap}
.service p{font-size:10.8px;line-height:12.3px;text-align:justify;color:#e6ecf8}
.service--narrow{width:238px}
</style>
</head>
<body>
<main class="canvas">

  <section class="flyer flyer--front">
    <div class="photo photo--family" role="img" aria-label="Photo of a smiling family giving thumbs up aboard a sailboat"></div>
    <svg class="wave" style="top:290px" width="400" height="80" viewBox="0 0 400 80">
      <path d="M0,38 C110,0 230,70 400,20 L400,80 L0,80Z" fill="#c9ccd3"/>
      <path d="M0,44 C110,8 230,76 400,28 L400,80 L0,80Z" fill="#ffffff"/>
      <path d="M0,54 C110,20 230,86 400,40 L400,80 L0,80Z" fill="#3a7bd0"/>
    </svg>

    <div class="polaroid" style="left:8px;top:270px;width:168px;height:152px;transform:rotate(-4deg)">
      <div class="shot" role="img" aria-label="Photo of a snorkeler swimming beside a stingray" style="background:linear-gradient(160deg,#8ccbd0,#4f8d8a 60%,#3c5f5c)"></div>
      <span class="pin" style="left:10px"></span>
    </div>
    <div class="polaroid" style="left:26px;top:400px;width:145px;height:135px;transform:rotate(-14deg)">
      <div class="shot" role="img" aria-label="Photo of two snorkelers underwater" style="background:linear-gradient(160deg,#2f9ad1,#1e6aa6)"></div>
      <span class="pin" style="left:112px"></span>
    </div>

    <div class="brand" style="right:16px;top:392px">
      <span class="brand-name">Driftwood Bay</span>
      <span class="brand-dot"></span>
    </div>

    <h1 class="headline">PRIVATE LUXURY<br><span class="accent">FULL DAY</span><br>GILDED GALLEY</h1>

    <p class="tagline">Experience yacht charter service at its Finest!</p>

    <p class="intro">Sail away with us on a Luxury Charter experience complete with a full brunch spread. During our sail we will take you to the hottest destination spots in the Caribbean surrounding St Thomas and St John. Warm, fresh baked afternoon cookies will be served on the way back from our days journeys. Unlimited water, sodas, beer and rum punch will be provided for the entire group to enjoy throughout the day.</p>

    <div class="lists">
      <div class="list">
        <h3>Our Unique Activities:</h3>
        <ul>
          <li>Snorkeling</li>
          <li>Underwater WaveGlider</li>
          <li>Cliff Diving</li>
          <li>Floating</li>
          <li>Paddleboard</li>
          <li>Site Seeing</li>
          <li>Tubing</li>
        </ul>
      </div>
      <div class="list">
        <h3>Harbor Fizz:</h3>
        <ul>
          <li>Up to 12 guests</li>
          <li>Assorted fruit tower</li>
          <li>Artesian Waffle</li>
          <li>Board, Frittata's</li>
          <li>Loaded Avocado Toast</li>
          <li>All American Breakfast</li>
          <li>Specialty Cocktails</li>
        </ul>
      </div>
    </div>

    <svg class="footer-band" width="400" height="80" viewBox="0 0 400 80">
      <path d="M0,14 C130,-4 270,-4 400,14 L400,80 L0,80Z" fill="#c9ccd3"/>
      <path d="M0,20 C130,2 270,2 400,20 L400,80 L0,80Z" fill="#ffffff"/>
    </svg>
    <div class="phone-pill">
      <svg width="18" height="18" viewBox="0 0 24 24" aria-hidden="true"><circle cx="12" cy="12" r="10.5" fill="none" stroke="#fff" stroke-width="2"/><path d="M8.5 6.5l2 2-1.2 1.6a7 7 0 0 0 4.6 4.6l1.6-1.2 2 2-1.4 1.8c-4.8-.4-8.9-4.5-9.3-9.3z" fill="#fff"/></svg>
      <span>(340) 555-0187</span>
    </div>
    <p class="contact">Info@driftwoodbayvoyages.example<span class="sep">|</span>driftwoodbayvoyages.example</p>
  </section>

  <section class="flyer flyer--back">
    <div class="photo photo--aerial" role="img" aria-label="Aerial photo of a catamaran over turquoise water beside a sandy beach"></div>
    <svg class="wave" style="top:190px" width="400" height="80" viewBox="0 0 400 80">
      <path d="M0,40 C90,-4 200,10 300,40 C340,52 370,50 400,44 L400,80 L0,80Z" fill="#c9ccd3"/>
      <path d="M0,46 C90,4 200,18 300,48 C340,60 370,58 400,52 L400,80 L0,80Z" fill="#ffffff"/>
      <path d="M0,56 C90,16 200,30 300,60 C340,72 370,70 400,64 L400,80 L0,80Z" fill="#3a7bd0"/>
    </svg>

    <div class="polaroid" style="left:286px;top:130px;width:122px;height:125px;transform:rotate(3deg)">
      <div class="shot" role="img" aria-label="Photo of guests toasting with drinks at a table aboard" style="background:linear-gradient(160deg,#d6c6a8,#b68a64 60%,#7e6a58)"></div>
      <span class="pin" style="left:8px"></span>
    </div>
    <div class="polaroid" style="left:262px;top:258px;width:140px;height:145px;transform:rotate(-6deg)">
      <div class="shot" role="img" aria-label="Photo of a snorkeler underwater" style="background:linear-gradient(160deg,#2a9fd0,#136e9e)"></div>
      <span class="pin" style="left:118px"></span>
    </div>
    <div class="polaroid" style="left:272px;top:400px;width:140px;height:145px;transform:rotate(12deg)">
      <div class="shot" role="img" aria-label="Photo of a sea turtle swimming over the reef" style="background:linear-gradient(160deg,#6fc6cf,#3a8fa3 60%,#6b8f6a)"></div>
      <span class="pin" style="left:10px"></span>
    </div>

    <div class="brand" style="left:20px;top:262px">
      <span class="brand-name">Driftwood Bay</span>
      <span class="brand-dot"></span>
    </div>

    <p class="intro-line">Driftwood Bay has just the<br>thing for you</p>

    <div class="services-tab">SERVICES OFFERED</div>

    <article class="service service--narrow" style="top:430px">
      <h2>Private Full Day Charter</h2>
      <p>You will be greeted with "Champagne Mimosas" as we welcome you on the boat. You will then be given a brief introduction to our boat, safety rules and procedures, and stateroom assignments</p>
    </article>

    <article class="service" style="top:536px">
      <h2>Private Half Day Charter</h2>
      <p>Our fully customizable itinerary will allow your group to do things like snorkeling, site seeing, or just relaxing. Some watersports that we have available on board include snorkel, underwater scooter, cliff diving, swimming, floating, paddleboard, and tubing.</p>
    </article>

    <article class="service" style="top:635px">
      <h2>Private Sunset and Bubbles Sail</h2>
      <p>Enjoy appetizers such as seasonal fruits, veggies and cured meats, and appetizers. While relaxing as our exceptional crew sails you through the coveted scenic spots in the USVI. As the sun sets, the drinks will flow.</p>
    </article>

    <article class="service" style="top:717px">
      <h2>Private Luxury Mini Overnight</h2>
      <p>Driftwood Bay offers a USVI Mini Overnight getaway. This charter can be booked solo, or combined with our above charter options to extend your time on the caribbean sea. Your luxury charter will start with a welcome "Champagne Cocktail," introduction to boat rules, safety and stateroom assignment</p>
    </article>

    <svg class="footer-band" width="400" height="80" viewBox="0 0 400 80">
      <path d="M0,14 C130,-4 270,-4 400,14 L400,80 L0,80Z" fill="#c9ccd3"/>
      <path d="M0,20 C130,2 270,2 400,20 L400,80 L0,80Z" fill="#ffffff"/>
    </svg>
    <div class="phone-pill">
      <svg width="18" height="18" viewBox="0 0 24 24" aria-hidden="true"><circle cx="12" cy="12" r="10.5" fill="none" stroke="#fff" stroke-width="2"/><path d="M8.5 6.5l2 2-1.2 1.6a7 7 0 0 0 4.6 4.6l1.6-1.2 2 2-1.4 1.8c-4.8-.4-8.9-4.5-9.3-9.3z" fill="#fff"/></svg>
      <span>(340) 555-0187</span>
    </div>
    <p class="contact">Info@driftwoodbayvoyages.example<span class="sep">|</span>driftwoodbayvoyages.example</p>
  </section>

</main>
</body>
</html>
```